A online shop for solid wood need a Stationary design

A new online shop (in Austria and Germany) for solid wood and steel furniture (feldmark-tischwerk) needs a Stationay design (letterhead, business card, envelope etc...). Dining tables, coffee tables, TV furniture and similar furniture will be sold. Everything will be custom made.

```html
<!DOCTYPE html>
<html lang="de">
<head>
<meta charset="utf-8">
<title>Feldmark Tischwerk – Visitenkarte</title>
<link rel="stylesheet" href="https://fonts.googleapis.com/css2?family=Montserrat:wght@400;500;700;800&display=swap">
<style>
  :root {
    --stage: #c4c4c4;
    --card-front: #2a2a2c;
    --card-back: #161617;
    --brand-red: #ec1c24;
    --text-light: #e6e6e6;
    --divider: #3a3a3d;
  }
  * { box-sizing: border-box; margin: 0; padding: 0; }
  html, body { width: 1200px; height: 800px; overflow: hidden; }
  body {
    background: radial-gradient(ellipse at 70% 20%, #d6d6d6 0%, var(--stage) 60%, #a9a9a9 100%);
    font-family: "Montserrat", Arial, sans-serif;
    position: relative;
  }
  .card {
    position: absolute;
    width: 540px;
    height: 310px;
    border-bottom: 3px solid var(--brand-red);
    box-shadow: 0 18px 40px rgba(0,0,0,0.35);
    overflow: hidden;
  }
  .card--front { left: 40px; top: 245px; background: var(--card-front); display: flex; }
  .card--back { left: 620px; top: 245px; background: var(--card-back); }

  .front__brand {
    width: 50%;
    display: flex;
    align-items: center;
    justify-content: center;
    gap: 14px;
    border-right: 1px solid var(--divider);
  }
  .brand-square { width: 34px; height: 34px; background: var(--brand-red); flex: none; }
  .brand-name {
    color: var(--brand-red);
    font-weight: 800;
    font-size: 24px;
    line-height: 1.05;
    letter-spacing: 1px;
    text-transform: uppercase;
  }
  .brand-name--small { font-size: 20px; }

  .front__contact {
    width: 50%;
    padding: 62px 20px 0 30px;
    color: var(--text-light);
  }
  .person-name {
    color: var(--brand-red);
    font-weight: 700;
    font-size: 18px;
    letter-spacing: 0.3px;
    text-transform: uppercase;
  }
  .person-role { font-size: 12.5px; margin-top: 2px; }
  .contact-list { list-style: none; margin-top: 18px; font-size: 11.5px; line-height: 1.6; }
  .contact-list li { display: flex; align-items: center; gap: 7px; white-space: nowrap; }
  .contact-list svg { width: 12px; height: 12px; flex: none; }
  .accent { color: var(--brand-red); }
  .address { font-size: 11.5px; line-height: 1.35; margin-top: 14px; padding-left: 19px; }

  .back__pattern {
    position: absolute;
    inset: 0;
    background: linear-gradient(200deg, #6e6e70 0%, #3a3a3c 30%, #1c1c1d 60%, #111 100%);
  }
  .back__brand {
    position: absolute;
    left: 50%;
    top: 50%;
    transform: translate(-50%, -50%);
    display: flex;
    align-items: center;
    gap: 12px;
  }
</style>
</head>
<body>
  <section class="card card--front">
    <div class="front__brand">
      <span class="brand-square"></span>
      <p class="brand-name">Feldmark<br>Tischwerk</p>
    </div>
    <div class="front__contact">
      <h1 class="person-name">Lukas Brenner</h1>
      <p class="person-role">Managing Director</p>
      <ul class="contact-list">
        <li>
          <svg viewBox="0 0 12 12"><path d="M3 1 L5 3.5 L4 4.8 Q5 7 7.2 8 L8.5 7 L11 9 L9.6 11 Q5 10.5 1 3 Z" fill="var(--brand-red)"/></svg>
          044-555 010 203
        </li>
        <li>
          <svg viewBox="0 0 12 12"><rect x="0.5" y="2.5" width="11" height="7" fill="var(--brand-red)"/><path d="M0.5 2.5 L6 7 L11.5 2.5" stroke="var(--card-front)" fill="none"/></svg>
          info@feldmark-tischwerk.com
        </li>
        <li>
          <svg viewBox="0 0 12 12"><circle cx="6" cy="6" r="5.2" fill="var(--brand-red)"/><path d="M1 6 H11 M6 1 V11 M6 1 Q2.5 6 6 11 M6 1 Q9.5 6 6 11" stroke="var(--card-front)" stroke-width="0.8" fill="none"/></svg>
          <span>www.<span class="accent">feldmark-tischwerk</span>.com</span>
        </li>
      </ul>
      <p class="address">12, Sägewerkstraße<br>4020 Linz, Austria</p>
    </div>
  </section>

  <section class="card card--back">
    <div class="back__pattern" role="img" aria-label="Embossed repeating brand pattern in dark grey tones"></div>
    <div class="back__brand">
      <span class="brand-square"></span>
      <p class="brand-name brand-name--small">Feldmark<br>Tischwerk</p>
    </div>
  </section>
</body>
</html>
```